i need a business card for a plumbing company in california

we are a drain cleaning , maintenance plumbing company who is starting new marketing campaign for a tatrench-less pipe installation department .

Target Market(s)

the professional who appreciates time and quality workmanship.

Industry/Entity Type

Plumbing

Colors
0655a3
ec1f27

Requirements
Must have
• the second logo needs to be included
Nice to have
• a focus on the services offered
Should not have
• any underlined words on the brief

```html
<!DOCTYPE html>
<html lang="en">
<head>
<meta charset="utf-8">
<title>Clearline Plumbing – Business Card</title>
<link href="https://fonts.googleapis.com/css2?family=Arimo:wght@400;700&display=swap" rel="stylesheet">
<style>
  :root {
    --brand-red: #e0282a;
    --ink-grey: #77776f;
    --text-grey: #666660;
    --paper: #ffffff;
    --backdrop: #2a2a2a;
    --faint-red: #fbe9e6;
  }
  * { box-sizing: border-box; margin: 0; padding: 0; }
  html, body { width: 1200px; height: 880px; overflow: hidden; }
  body {
    background: var(--backdrop);
    font-family: "Arimo", Arial, sans-serif;
    position: relative;
  }
  .card {
    position: absolute;
    width: 630px;
    height: 360px;
    border-radius: 22px;
    overflow: hidden;
  }

  /* Front side */
  .card-front {
    left: 90px; top: 70px;
    background: var(--brand-red);
    display: flex; align-items: center; justify-content: center;
  }
  .wordmark {
    display: flex; align-items: center; gap: 16px;
  }
  .wordmark-square {
    width: 34px; height: 34px;
  }
  .wordmark-name {
    font-weight: 700;
    font-size: 46px;
    line-height: 1;
    letter-spacing: 0.5px;
  }
  .card-front .wordmark-square { background: var(--paper); }
  .card-front .wordmark-name { color: var(--paper); }

  /* Back side */
  .card-back {
    left: 480px; top: 450px;
    background: var(--paper);
  }
  .card-back .wordmark {
    position: absolute; left: 56px; top: 58px;
  }
  .card-back .wordmark-square { background: var(--brand-red); width: 28px; height: 28px; }
  .card-back .wordmark-name { color: var(--ink-grey); font-size: 38px; }

  .faint-mark {
    position: absolute; right: 40px; top: 20px;
    width: 170px; height: 170px; border-radius: 50%;
    background: var(--faint-red);
  }
  .edge-dot {
    position: absolute; left: -22px; top: 190px;
    width: 44px; height: 44px; border-radius: 50%;
    background: var(--brand-red);
  }
  .divider {
    position: absolute; left: 150px; right: 30px; top: 244px;
    height: 2px; background: var(--brand-red);
  }
  .person {
    position: absolute; left: 150px; top: 196px;
  }
  .person-name {
    color: var(--brand-red); font-weight: 700; font-size: 22px; line-height: 1.05;
  }
  .person-role {
    color: var(--text-grey); font-size: 16px; line-height: 1.1;
  }
  .contacts {
    position: absolute; left: 150px; top: 258px;
    list-style: none;
  }
  .contacts li {
    display: flex; align-items: center; gap: 8px;
    color: var(--text-grey); font-size: 17px; line-height: 24px;
  }
  .contacts svg { width: 16px; height: 16px; flex: none; }
  .address {
    position: absolute; right: 36px; top: 256px;
    text-align: right;
    color: var(--text-grey); font-size: 16px; line-height: 21px;
  }
  .band-grey {
    position: absolute; left: 0; bottom: 0;
    width: 322px; height: 22px; background: var(--ink-grey);
  }
  .band-red {
    position: absolute; right: 0; bottom: 0;
    width: 296px; height: 44px; background: var(--brand-red);
    color: var(--paper); font-size: 16px;
    display: flex; align-items: center; justify-content: flex-end;
    padding-right: 36px;
  }
</style>
</head>
<body>

<section class="card card-front" aria-label="Card front">
  <div class="wordmark">
    <span class="wordmark-square"></span>
    <span class="wordmark-name">Clearline Plumbing</span>
  </div>
</section>

<section class="card card-back" aria-label="Card back">
  <div class="faint-mark"></div>
  <div class="wordmark">
    <span class="wordmark-square"></span>
    <span class="wordmark-name">Clearline Plumbing</span>
  </div>

  <div class="edge-dot"></div>

  <div class="person">
    <p class="person-name">Dana Whitfield</p>
    <p class="person-role">Manager</p>
  </div>
  <div class="divider"></div>

  <ul class="contacts">
    <li>
      <svg viewBox="0 0 16 16" aria-hidden="true"><circle cx="8" cy="8" r="8" fill="#e0282a"/><path d="M5 4.5c.6-.3 1 .1 1.3.8l.4.9c.2.5 0 .8-.4 1.1.4.8 1 1.4 1.8 1.8.3-.4.6-.6 1.1-.4l.9.4c.7.3 1.1.7.8 1.3-.4.8-1.2 1.2-2.1.9C7.1 10.6 5.4 8.9 4.7 7 4.4 6 4.4 5 5 4.5z" fill="#fff"/></svg>
      555-014-2290
    </li>
    <li>
      <svg viewBox="0 0 16 16" aria-hidden="true"><circle cx="8" cy="8" r="8" fill="#e0282a"/><rect x="4" y="5.2" width="8" height="5.6" rx="0.6" fill="#fff"/><path d="M4.3 5.6 8 8.4l3.7-2.8" fill="none" stroke="#e0282a" stroke-width="0.9"/></svg>
      hello@clearlineplumb.com
    </li>
  </ul>

  <p class="address">PO BOX 48 Harbor Road<br>Riverside, California</p>

  <div class="band-grey"></div>
  <div class="band-red">www.clearlineplumb.com</div>
</section>

</body>
</html>
```